Design a Consultation and HR Services Website "Bright Paths"

Consultation and HR Services
I am looking for a design gives the look and feel of Varden Holt and Quillmere
we need a high-quality graphics website that looks rich and expensive.
we are working as an affiliate for international consultation firms and sole agent for international HR products.
we are a group of consultants for the Middle East.
we will get the global practices to local practices.
Updates

Project Deadline Extended
Reason: I am not getting enough options and designs. I am not getting what I was looking for in matter of look and feel. looking for something rich and luxury with black background and rich font. www.gridmarlow.com www.benitavoss.com 17kendalrow.com/ www.trulo.cc/rd/en/ pemberfold.com/ www.trulo.cc/rd/en/ www.zolmi.com/ www.thegildings.co.uk/ .

Target Market(s)

Corporate all size and industries in GCC

Industry/Entity Type

Management Consulting

Coding

Coded - Design and coding required

Number of Pages Required

5+ page

Font styles to use
Sans Serif
Script

Colors
ffffff
ecf7fb
cee9f5
85cae6
33a6d7
0592cd
000000
848484

Requirements
Must have
• This is the looks and feel that I'm looking for.
• http://www.gridmarlow.com/?channel=display&subchannel=pagemuse
• http://www.benitavoss.com/bvny-private/en/
• http://17kendalrow.com/
• http://www.trulo.cc/rd/en/
• http://pemberfold.com/
• http://www.zolmi.com/
• http://www.thegildings.co.uk/
• Home
• Who we are?
• What we do?
• HR & OD Consultation
• Executive Coaching
• Assesment Cemter
• HRIS & Outsourcing
• Testimonials
• Our Partners
• Contact Us
• We need support on Technical righting...

```html
<!DOCTYPE html>
<html lang="en">
<head>
<meta charset="utf-8">
<title>Bright Paths — Consultation and HR Services</title>
<link rel="stylesheet" href="https://fonts.googleapis.com/css2?family=Open+Sans:wght@300;400;600&family=Oswald:wght@300;400&family=Raleway:wght@400;500&display=swap">
<style>
:root{
  --black:#000000;
  --ink:#1b1f23;
  --ink-deep:#15181b;
  --blue:#1fa2d3;
  --blue-dark:#0592cd;
  --blue-soft:#85cae6;
  --pale:#ecf7fb;
  --grey:#848484;
  --text:#555;
  --white:#ffffff;
}
*{box-sizing:border-box;margin:0;padding:0}
html,body{width:1200px;height:2311px;overflow:hidden}
body{position:relative;background:var(--white);font-family:"Open Sans",Arial,sans-serif;color:var(--text)}
.abs{position:absolute}

/* header */
.topbar{left:0;top:0;width:1200px;height:128px;background:var(--black);border-top:3px solid var(--blue)}
.brand{left:97px;top:40px;display:flex;align-items:center;gap:12px}
.brand-mark{width:34px;height:34px;border:3px solid var(--blue)}
.brand-name{font:600 27px "Open Sans",sans-serif;color:var(--blue);letter-spacing:1px}
.search{left:771px;top:45px;width:330px;height:43px;border:1px solid #555;border-radius:3px;display:flex;align-items:center;justify-content:space-between;padding:0 14px;color:#777;font-size:13px}
.mainnav{left:0;top:128px;width:1200px;height:65px;background:var(--blue)}
.mainnav ul{list-style:none;display:flex;position:absolute;left:100px;top:0;height:65px}
.mainnav li{height:65px;line-height:65px;font-size:14px;color:var(--white);text-align:center}
.mainnav li.active{background:#a9b3b8}

/* hero */
.hero{left:0;top:193px;width:1200px;height:553px;background:linear-gradient(90deg,#cfcdc8 0%,#c3c1bb 55%,#b4b1aa 100%)}
.hero-art{left:570px;top:0;width:630px;height:553px;background:radial-gradient(ellipse at 45% 55%,#8d8a84 0%,#aeaba5 45%,rgba(190,188,182,0) 75%)}
.hero-title{left:112px;top:340px;font:400 56px "Raleway",sans-serif;color:var(--blue)}
.hero-sub{left:116px;top:410px;font:italic 300 17px "Open Sans",sans-serif;color:#444}
.hero-text{left:116px;top:447px;width:455px;font-size:14px;line-height:20px;color:#333}
.hero-btn{left:117px;top:544px;width:145px;height:38px;background:var(--blue);color:var(--white);font-size:16px;line-height:38px;text-align:center}
.hero-arrow{top:472px;width:30px;height:30px}

/* welcome + services */
.welcome{left:0;top:746px;width:550px;height:406px;background:var(--blue);color:var(--white)}
.welcome h2{position:absolute;left:98px;top:44px;font:300 27px "Oswald",sans-serif}
.rule{position:absolute;height:2px;width:90px}
.welcome .rule{left:98px;top:96px;background:var(--white)}
.welcome p{position:absolute;left:98px;top:136px;width:388px;font-size:12px;line-height:20.5px;text-align:justify}
.btn-outline{position:absolute;left:98px;top:318px;width:155px;height:36px;border:1px solid var(--white);font-size:13px;line-height:34px;text-align:center}
.services{left:550px;top:746px;width:650px;height:406px;background:#f7f8f8}
.services h2{position:absolute;left:70px;top:44px;font:300 27px "Oswald",sans-serif;color:#333}
.services .rule{left:70px;top:96px;background:#333;width:52px}
.svc{position:absolute;width:230px}
.svc h3{display:flex;align-items:center;gap:18px;font:400 15px "Open Sans",sans-serif;color:var(--blue);height:30px}
.svc p{margin-top:12px;font-size:12px;line-height:19px;color:#444}

/* about row */
.pillar{top:1207px;width:300px}
.pillar h3{display:flex;align-items:center;font:400 26px "Open Sans",sans-serif;color:#222}
.pillar .initial{width:46px;height:38px;border:1.5px solid var(--blue);color:var(--blue);text-align:center;line-height:36px;margin-right:10px}
.pillar p{margin-top:22px;font-size:12px;line-height:20px;color:#555}

/* features */
.features{left:0;top:1394px;width:1200px;height:549px;background:radial-gradient(ellipse at 20% 40%,#eaf3f8 0%,#f6fafc 55%,#fbfdfe 100%);border-top:1px solid #eef2f4}
.features h2{position:absolute;left:97px;top:46px;font:300 27px "Oswald",sans-serif;color:var(--blue)}
.features .rule{left:97px;top:97px;background:var(--blue)}
.card{position:absolute;top:143px;width:318px}
.card-img{width:318px;height:216px;border:5px solid var(--white);box-shadow:0 0 0 1px #e3e6e8}
.card h3{margin-top:26px;padding-left:4px;font:400 21px "Open Sans",sans-serif;color:#222}
.card p{margin-top:8px;padding-left:4px;font-size:12px;line-height:20px;color:#555}

/* footer */
.footer{left:0;top:1943px;width:1200px;height:302px;background:var(--ink);color:#9aa0a5}
.footer h4{position:absolute;top:56px;font:300 23px "Oswald",sans-serif;color:var(--white)}
.footer .brand-foot{font:600 24px "Open Sans",sans-serif;letter-spacing:1px}
.footer p{position:absolute;font-size:12px;line-height:20px}
.social{position:absolute;left:99px;top:211px;display:flex;gap:9px}
.social span{width:18px;height:18px;background:#6b7278}
.contact-line{position:absolute;left:868px;display:flex;align-items:center;gap:18px;font-size:14px}
.bottombar{left:0;top:2245px;width:1200px;height:66px;background:var(--ink-deep);color:#9aa0a5;font-size:12px;line-height:66px;padding-left:96px}
</style>
</head>
<body>

<header class="abs topbar">
  <div class="abs brand"><span class="brand-mark"></span><span class="brand-name">Bright Paths</span></div>
  <div class="abs search">
    <svg width="14" height="14" viewBox="0 0 14 14"><circle cx="6" cy="6" r="4.2" fill="none" stroke="#888" stroke-width="1.6"/><line x1="9" y1="9" x2="13" y2="13" stroke="#888" stroke-width="1.6"/></svg>
    <span>Search</span>
  </div>
</header>

<nav class="abs mainnav">
  <ul>
    <li class="active" style="width:134px">Home</li>
    <li style="width:137px">About Us</li>
    <li style="width:142px">Features</li>
    <li style="width:155px">Our Services</li>
    <li style="width:146px">Our Blog</li>
    <li style="width:104px">News</li>
    <li style="width:160px">Contact Us</li>
  </ul>
</nav>

<section class="abs hero">
  <div class="abs hero-art" role="img" aria-label="Businessman on a ladder drawing a tree of symbols and numbers on a concrete wall"></div>
</section>
<h1 class="abs hero-title">Bright Paths</h1>
<p class="abs hero-sub">We are a Consultation and HR Services company</p>
<p class="abs hero-text">Eiusmod tempor incididunt ut labore et dolore magna aliqua. Ut enim ad minim veniam, quis nostrud exercitation ullamco laboris nisi ut aliquip ex ea commodo consequat</p>
<div class="abs hero-btn">Contact Us</div>
<svg class="abs hero-arrow" style="left:37px" viewBox="0 0 30 30"><circle cx="15" cy="15" r="13" fill="none" stroke="#555" stroke-width="1.5"/><polyline points="17,9 11,15 17,21" fill="none" stroke="#555" stroke-width="1.8"/></svg>
<svg class="abs hero-arrow" style="left:1133px" viewBox="0 0 30 30"><circle cx="15" cy="15" r="13" fill="none" stroke="#555" stroke-width="1.5"/><polyline points="13,9 19,15 13,21" fill="none" stroke="#555" stroke-width="1.8"/></svg>

<section class="abs welcome">
  <h2>Welcome to Bright Paths</h2>
  <span class="rule"></span>
  <p>I must explain to you how all this mistaken idea of denouncing pleasure and praising pain was born and I will give you a complete account of the system, and expound the actual teachings of the great explorer of the truth, the master-builder of human happiness. No one rejects, dislikes, or avoids pleasure itself, because it is pleasure, but because those who do not know how to pursue pleasure rationally encounter consequences that are extremely painful.</p>
  <div class="btn-outline">Read More About Us</div>
</section>

<section class="abs services">
  <h2>Our Service</h2>
  <span class="rule"></span>
  <div class="svc" style="left:68px;top:128px">
    <h3><svg width="30" height="26" viewBox="0 0 30 26"><polyline points="2,2 2,24 28,24" fill="none" stroke="#999" stroke-width="2"/><polyline points="5,20 12,12 17,16 26,5" fill="none" stroke="#999" stroke-width="2"/></svg>Business Consultation</h3>
    <p>Neque porro quisquam est, qui dolorem ipsum quia doloramet, consectetur, adipisci velit, sed ...</p>
  </div>
  <div class="svc" style="left:325px;top:128px">
    <h3><svg width="24" height="28" viewBox="0 0 24 28"><circle cx="12" cy="8" r="6" fill="#999"/><path d="M1 27 Q1 15 12 15 Q23 15 23 27 Z" fill="#999"/></svg>HR Services</h3>
    <p>Neque porro quisquam est, qui dolorem ipsum quia doloramet, consectetur, adipisci velit, sed ...</p>
  </div>
  <div class="svc" style="left:68px;top:257px">
    <h3><svg width="28" height="28" viewBox="0 0 28 28"><circle cx="14" cy="14" r="12" fill="none" stroke="#999" stroke-width="2"/><ellipse cx="14" cy="14" rx="5" ry="12" fill="none" stroke="#999" stroke-width="1.6"/><line x1="2" y1="14" x2="26" y2="14" stroke="#999" stroke-width="1.6"/></svg>Online Consultation</h3>
    <p>Neque porro quisquam est, qui dolorem ipsum quia doloramet, consectetur, adipisci velit, sed ...</p>
  </div>
  <div class="svc" style="left:325px;top:257px">
    <h3><svg width="26" height="26" viewBox="0 0 26 26"><rect x="2" y="3" width="22" height="15" rx="1" fill="none" stroke="#999" stroke-width="2"/><rect x="9" y="20" width="8" height="3" fill="#999"/></svg>IT Managements</h3>
    <p>Neque porro quisquam est, qui dolorem ipsum quia doloramet, consectetur, adipisci velit, sed ...</p>
  </div>
</section>

<article class="abs pillar" style="left:97px">
  <h3><span class="initial">A</span>BOUT US</h3>
  <p>Nemo enim ipsam voluptatem quia voluptas sit aspernatur aut odit aut fugit, sed quia consequuntur magni dolores eos qui ratione voluptatem sequi nesciunt. Neque porro quisquam est, qui dolorem...</p>
</article>
<article class="abs pillar" style="left:454px">
  <h3><span class="initial">M</span>OTIVATION</h3>
  <p>Nemo enim ipsam voluptatem quia voluptas sit aspernatur aut odit aut fugit, sed quia consequuntur magni dolores eos qui ratione voluptatem sequi nesciunt. Neque porro quisquam est, qui dolorem...</p>
</article>
<article class="abs pillar" style="left:810px">
  <h3><span class="initial">H</span>ISTORY</h3>
  <p>Nemo enim ipsam voluptatem quia voluptas sit aspernatur aut odit aut fugit, sed quia consequuntur magni dolores eos qui ratione voluptatem sequi nesciunt. Neque porro quisquam est, qui dolorem...</p>
</article>

<section class="abs features">
  <h2>Our Features</h2>
  <span class="rule"></span>
  <div class="card" style="left:97px">
    <div class="card-img" role="img" aria-label="Two consultants in conversation at an office desk" style="background:linear-gradient(135deg,#dfe9f1 0%,#a9c4dc 50%,#5f86b3 100%)"></div>
    <h3>Denouncing Pleasure</h3>
    <p>Perspiciatis unde omnis iste natus error sit voluptatem accusantium doloremque laudantium, totam rem aperiam, eaque ipsa quae ab illo inventore veritatis et quasi architecto beatae vitae dicta sunt explicabo.</p>
  </div>
  <div class="card" style="left:440px">
    <div class="card-img" role="img" aria-label="Blue business infographic tiles with cloud, puzzle and idea icons" style="background:linear-gradient(135deg,#4fb8ee 0%,#cde9f8 50%,#1f9be0 100%)"></div>
    <h3>Dolorem Ipsum</h3>
    <p>Perspiciatis unde omnis iste natus error sit voluptatem accusantium doloremque laudantium, totam rem aperiam, eaque ipsa quae ab illo inventore veritatis et quasi architecto beatae vitae dicta sunt explicabo.</p>
  </div>
  <div class="card" style="left:786px">
    <div class="card-img" role="img" aria-label="Hands cupped around a person icon within a network of people" style="background:linear-gradient(135deg,#1c2636 0%,#34465e 50%,#121923 100%)"></div>
    <h3>Voluptas Assumenda</h3>
    <p>Perspiciatis unde omnis iste natus error sit voluptatem accusantium doloremque laudantium, totam rem aperiam, eaque ipsa quae ab illo inventore veritatis et quasi architecto beatae vitae dicta sunt explicabo.</p>
  </div>
</section>

<footer class="abs footer">
  <h4 class="brand-foot" style="left:97px">Bright Paths</h4>
  <p style="left:99px;top:110px;width:320px">Perspiciatis unde omnis iste natus error sit voluptatem accusantium doloremque laudantium, totam rem aperiam, eaque ipsa quae ab illo inventore veritatis et quasi architecto beatae vitae dicta sunt explicabo...</p>
  <div class="social"><span></span><span></span><span></span><span></span></div>

  <h4 style="left:490px">Teastimonial</h4>
  <p style="left:493px;top:110px;width:310px">Perspiciatis unde omnis iste natus error sit voluptatem accusantium doloremque laudantium, totam rem aperiam, eaque ipsa quae ab illo inventore veritatis et quasi architecto beatae vitae dicta sunt explicabo... "</p>
  <p style="left:493px;top:214px;font-size:11px;font-style:italic">- Lena Marsh</p>
  <p style="left:587px;top:214px;font-size:11px;font-style:italic;color:var(--blue)">View All Testimonial</p>

  <h4 style="left:868px;top:53px">Contact Us</h4>
  <p style="left:868px;top:108px;width:240px">Sit voluptatem accusantium doloremque laudantium, totam rem aperiam</p>
  <div class="contact-line" style="top:164px">
    <svg width="16" height="16" viewBox="0 0 16 16"><path d="M3 1 L6 1 L7 5 L5 6 Q6 9 10 11 L11 9 L15 10 L15 13 Q14 15 12 15 Q2 13 1 3 Q1 1 3 1 Z" fill="#9aa0a5"/></svg>
    <span>+2515550142/1255550187</span>
  </div>
  <div class="contact-line" style="top:199px">
    <svg width="16" height="16" viewBox="0 0 16 16"><path d="M2 14 L3 10 L11 2 L14 5 L6 13 Z" fill="#9aa0a5"/></svg>
    <span>info@brightpaths.com</span>
  </div>
</footer>

<div class="abs bottombar">Copyrights@bright paths 2015</div>

</body>
</html>
```